Kelvane Plumbing Business cards

Company is Kelvane Plumbing.
name Dashel Morrowby, I am a plumber, drainer, gasfitter and roofer
Mobile: 0431 906 154
Email address: info@kelvaneplumbing.example (check out my website for some ideas)
Website: www.kelvaneplumbing.example
ABN: 82 916 203 471
LIC: 604517K

I am reliable all round plumber. I am a 24 hour emergency service. Kelvane Plumbing is a professional plumbing service in the Illawarra, South Coast, Southern Sydney and Southern Highland regions of NSW. We offer a 24 hour emergency service for piece of mind to our customers. Call us now to see how we can help you. Kelvane Plumbing approaches every job with attention to detail and excellent customer service. With our superior workmanship you can be confident that the job will be done right the first time around. You can rest assured with results that are guaranteed to last.

Target Market(s)

the general public

Contact Information for Business Card

look up website for some ideas something with similar colours to logo and new modern and to catch the eye.

Colors
fdfdfd
ffffff
000000
7f7f7f
aaaaaa
33a6d7
0492cd

Requirements
Must have
• all contact details
• company- Kelvane Plumbing
• name- Dashel Morrowby
• number mobile- 0431 906 154
• Email address- info@kelvaneplumbing.example
• Website- www.kelvaneplumbing.example
• ABN- 82 916 203 471
• LIC- 604517K

```html
<!DOCTYPE html>
<html lang="en">
<head>
<meta charset="UTF-8">
<title>Kelvane Plumbing Business Cards</title>
<link href="https://fonts.googleapis.com/css2?family=Poppins:wght@400;500;600&display=swap" rel="stylesheet">
<style>
  :root {
    --stage: #1c1c1c;
    --card: #2a2a2b;
    --blue: #0492cd;
    --blue-light: #33a6d7;
    --white: #fdfdfd;
    --grey: #7f7f7f;
    --grey-light: #aaaaaa;
  }
  * { margin: 0; padding: 0; box-sizing: border-box; }
  html, body {
    width: 1200px; height: 900px; overflow: hidden;
    background: var(--stage);
    font-family: "Poppins", sans-serif;
  }
  .stage {
    position: relative; width: 1200px; height: 900px;
    display: flex; flex-direction: column; align-items: center; justify-content: center; gap: 40px;
  }
  .card {
    position: relative; width: 560px; height: 320px;
    background: var(--card);
    overflow: hidden;
    box-shadow: 0 10px 30px rgba(0,0,0,.45);
  }
  /* Brand */
  .brand { display: flex; align-items: center; gap: 12px; }
  .brand-dot {
    width: 16px; height: 16px; border-radius: 50%;
    background: var(--blue); flex: none;
  }
  .brand-name {
    font-weight: 600; color: var(--blue-light);
    letter-spacing: .04em; text-transform: uppercase; white-space: nowrap;
  }
  /* Front */
  .card-front .brand {
    position: absolute; top: 112px; left: 0; right: 0; justify-content: center;
  }
  .card-front .brand-name { font-size: 30px; }
  .info-band {
    position: absolute; left: 0; right: 0; bottom: 24px; height: 34px;
    background: var(--blue);
    display: flex; align-items: center; justify-content: center; gap: 10px;
    color: var(--white); font-size: 13px; white-space: nowrap;
  }
  .info-band strong { font-weight: 600; }
  /* Back */
  .card-back .brand {
    position: absolute; top: 128px; left: 40px;
  }
  .card-back .brand-name { font-size: 22px; }
  .person {
    position: absolute; top: 40px; right: 40px; text-align: right;
  }
  .person-name {
    font-size: 16px; font-weight: 500; letter-spacing: .03em; color: var(--white);
    text-transform: uppercase;
  }
  .person-name .first { color: var(--blue-light); font-weight: 600; }
  .person-role { font-size: 12px; color: var(--grey); margin-top: -2px; }
  .person-rule {
    position: absolute; top: 86px; right: 70px; width: 200px; height: 1px;
    background: var(--blue);
  }
  .contact-rule {
    position: absolute; left: 40px; bottom: 118px; width: 270px; height: 1px;
    background: var(--blue);
  }
  .contacts {
    position: absolute; left: 40px; bottom: 28px; list-style: none;
    display: flex; flex-direction: column; gap: 6px;
  }
  .contact {
    display: flex; align-items: center; gap: 12px;
    font-size: 14px; color: var(--white);
  }
  .contact-icon {
    width: 18px; height: 18px; border-radius: 50%;
    background: var(--blue); display: flex; align-items: center; justify-content: center;
    flex: none;
  }
</style>
</head>
<body>
<main class="stage">

  <section class="card card-front" aria-label="Card front">
    <div class="brand">
      <span class="brand-dot"></span>
      <span class="brand-name">Kelvane Plumbing</span>
    </div>
    <div class="info-band">
      <span><strong>ABN</strong> - 82 916 203 471</span>
      <span>|</span>
      <span><strong>24*7</strong> Emergency Service</span>
      <span>|</span>
      <span><strong>LIC</strong> - 604517K</span>
    </div>
  </section>

  <section class="card card-back" aria-label="Card back">
    <div class="person">
      <p class="person-name"><span class="first">Dashel</span> Morrowby</p>
      <p class="person-role">Founder</p>
    </div>
    <div class="person-rule"></div>

    <div class="brand">
      <span class="brand-dot"></span>
      <span class="brand-name">Kelvane Plumbing</span>
    </div>

    <div class="contact-rule"></div>
    <ul class="contacts">
      <li class="contact">
        <span class="contact-icon">
          <svg width="10" height="10" viewBox="0 0 24 24" aria-hidden="true"><path fill="#fdfdfd" d="M6.6 10.8a15 15 0 0 0 6.6 6.6l2.2-2.2a1 1 0 0 1 1-.25 11.4 11.4 0 0 0 3.6.57 1 1 0 0 1 1 1V20a1 1 0 0 1-1 1A17 17 0 0 1 3 4a1 1 0 0 1 1-1h3.5a1 1 0 0 1 1 1c0 1.250.2 2.450.57 3.57a1 1 0 0 1-.25 1z"/></svg>
        </span>
        <span>0431 - 906 - 154</span>
      </li>
      <li class="contact">
        <span class="contact-icon">
          <svg width="10" height="10" viewBox="0 0 24 24" aria-hidden="true"><path fill="#fdfdfd" d="M2 5h20v14H2z"/><path fill="none" stroke="#0492cd" stroke-width="2" d="M2 5l10 8 10-8"/></svg>
        </span>
        <span>info@kelvaneplumbing.example</span>
      </li>
      <li class="contact">
        <span class="contact-icon">
          <svg width="11" height="11" viewBox="0 0 24 24" aria-hidden="true"><circle cx="12" cy="12" r="9" fill="none" stroke="#fdfdfd" stroke-width="2"/><path fill="none" stroke="#fdfdfd" stroke-width="1.6" d="M3 12h18M12 3c3 3 3 15 0 18M12 3c-3 3-3 15 0 18"/></svg>
        </span>
        <span>www.kelvaneplumbing.example</span>
      </li>
    </ul>
  </section>

</main>
</body>
</html>
```